We need a range of stationery items designed for our active, community-orientated, out-going, all-age, family-friendly church in central Auckland, New Zealand.
We want to refresh and modernize the branding/images for Kereru Gospel Chapel itself so this image reflects who we are and our values.
Our church is located on a very busy intersection in the heart of a multi-ethnic local community. A number of churches and other groups use our site so we have branded our site as "The Meeting Pole". We have an existing logo for "The Meeting Pole" (see attached).
We would like you to design 4 items: a Letterhead, a With Compliments slip, a Business Card, and the Front Cover of our church newsletter, but we've included a request for an Email signature as an optional extra for this brief.
Organisation Details:
Name: Kereru Gospel Chapel
Postal Address: PO Box 38514, Wharenui, Auckland 1893
Email: office@kererugospel.org.nz
Phone: 09 473 5619
Web: www.kererugospel.org.nz (current website will be changed)
Position Statement: "a place of hope, belonging and worship"
Fonts:
The fonts for the "The Meeting Pole" logo are Futura Medium BT and Futura Lt BT. We would like the Futura font family used in the designs but feel free to add other fonts as appropriate (preferably True Type open source ones).
Colours:
Our current external signage colours are Dark Grey (Tolvar Coatings 'Slatewick' - RGB 57-55-53 ) and orange ( Tolvar 'Sunflare' - RGB 255-82-0 ). These are the colours for 'The Meeting Pole' which is our site. As we have other churches using our premises also we are looking to create a separate but complimentary identity for Kereru Gospel Chapel with a different colour set. We would ideally like a primary colour, a complimentary colour and an offset colour.
Design:
For the Kereru Gospel Chapel stationary we want the design to incorporate some of the elements of the 'Meeting Pole' particularly the extended 'T' device, so that we develop a separate identity but in the same family. We would like something that will look good for a number of years, rather than something that will date quickly in a year or two as fashions change.
PROJECTS
1. Letterhead
Finished size A4 (210 mm wide x 297mm tall)
This will become a template in MSWord. It will be printed in colour on our office photocopier so it must have a 5mm white border around the entire outside edge of the A4 page. "The Meeting Pole" logo needs to be incorporated in some form on the page.
2. With Compliments slip
Finished size 210 mm wide x 99 mm tall
This will be printed in colour on our office photocopier so it must have a 5mm white border around the entire outside edge of the slip. We will print these slips 3-up on an A4 page. The actual design space will be 200mm x 89mm. It is envisaged that this slip will use the same elements as the letterhead design. Please supply two versions, with and without the words "With Compliments".
3. Business Card
Finished size 90 mm wide by 55 mm tall.
This will be printed by commercial printers so colours can run to the edge of the card. Your Kereru Gospel Logo with the extended 'T' devise will need to feature on this.
4. Front Cover of Church Newsletter
Finished size 100 mm wide x 210 mm tall.
Our newsletter is printed in landscape on A4 paper and is folded twice.
It will be printed in colour on our office photocopier so it will need to have a minimum 5mm white border on all 4 sides. Attractive inviting colours preferred.
Needs to have:
- a place for the words Sunday and a date (which will change each Sunday)
- your Kereru Gospel Logo with the extended 'T' devise
- the words Sundays @ 10am
- the words ""a place of hope, belonging and worship"
- optional - "The Meeting Pole" logo (background does not need to be black)
5. Email Signature - optional extra
Not too large but something that will enable those receiving emails to instantly recognize who the email is from. Needs to include your Kereru Gospel logo, the name of the person, their position and our contact details.
Reason: We are extending the deadline on this project in order to encourage a broader range of designs, both from those who have already submitted designs and from those who are considering entering our competition. We'd love to see what you have to offer so please do submit your designs.
Re: Stationery for Kereru Gospel Chapel
Thanks to all the designers who have submitted designs for our competition so far. We have refrained from requesting a whole lot of tweaks to individual designs out of respect for your time as we understand that you are all busy professionals and that design competitions like this are just one way that you pitch for new business.
We would though like to offer some general comments on the submissions that we have seen so far. One thing that we would definitely like to arrive at via this process is to decide on a colour scheme. For this, as per the brief notes ( but possibly obscured by some of the other detail ) we want to have a primary colour and an offset colour and also an accent colour in the pallet.
Another thing that we maybe didn't make clear enough is that the colours for the identity of the site, known as The Meeting Pole, uses dark grey and orange but that we wanted to develop a separate but related identity for Kereru Gospel Chapel that meets there as we also now have other congregations that use our buildings.
One of the keys for the new identity will be the new colour pallet which we wanted to steer away from the darker tones that we used for the site branding. Therefore we would very much like to see your suggestions one or two secondary colours along with the primary brand colour if possible please.
Thank you all once again.
Kind regards

```html
<!DOCTYPE html>
<html lang="en">
<head>
<meta charset="utf-8">
<title>Kereru Gospel Chapel – Stationery</title>
<link rel="stylesheet" href="https://fonts.googleapis.com/css2?family=Jost:wght@400;500;700&family=Alegreya:wght@400;700&family=Open+Sans:wght@400;600;700&family=Montserrat:wght@700&family=Courgette&display=swap">
<style>
:root{
  --blue-deep:#1a6496;
  --blue-mid:#1f7fc0;
  --blue-bright:#2596d9;
  --ink:#1d1d1f;
  --paper:#ffffff;
  --edge:#c9c9c9;
  --pale:#e6f1f9;
  --brand-grad:linear-gradient(90deg,var(--blue-deep),var(--blue-bright));
  --bar-grad:linear-gradient(180deg,var(--blue-bright),var(--blue-deep));
}
*{box-sizing:border-box;margin:0;padding:0}
html,body{width:1200px;height:1000px;overflow:hidden;background:var(--paper)}
body{position:relative;font-family:'Open Sans',sans-serif;color:var(--ink)}
.sheet{position:absolute;background:var(--paper);border:1px solid var(--edge);overflow:hidden}
.bar-v{position:absolute;top:0;bottom:0;background:var(--bar-grad)}
.bar-h{position:absolute;background:var(--blue-bright)}
.mark{position:absolute;background:var(--blue-mid)}
.wordmark{position:absolute;font-family:'Jost',sans-serif;font-weight:400;color:var(--blue-deep);white-space:nowrap;line-height:1}
.contact{position:absolute;font-family:'Alegreya',serif;font-size:7.5px;line-height:9.5px;color:var(--ink)}
.web{position:absolute;font-family:'Alegreya',serif;font-weight:700;font-size:7.5px;color:var(--ink)}

/* Letterhead */
.letterhead{left:49px;top:37px;width:487px;height:689px}
.letterhead .bar-v{left:36px;width:8px}
.letterhead .bar-h{left:6px;top:64px;width:72px;height:7px}
.letterhead .mark{left:85px;top:43px;width:42px;height:42px}
.letterhead .wordmark{left:137px;top:55px;font-size:22px}
.letterhead .contact{left:85px;top:641px}
.letterhead .web{left:348px;top:641px}

/* Newsletter cover */
.newsletter{left:571px;top:37px;width:268px;height:564px;border:none}
.newsletter .header{position:absolute;left:0;top:0;width:268px;height:104px;background:var(--brand-grad)}
.newsletter .bar-v{left:15px;width:7px}
.newsletter .bar-h{left:4px;top:33px;width:32px;height:6px;background:rgba(255,255,255,.35)}
.newsletter .date{position:absolute;right:14px;top:13px;font-family:'Alegreya',serif;font-weight:700;font-size:7.5px;color:#fff}
.newsletter .mark{left:50px;top:24px;width:40px;height:40px;background:#fff}
.newsletter .wordmark{left:96px;top:38px;font-size:15px;color:#fff}
.newsletter .tagline{position:absolute;left:0;right:0;top:80px;text-align:center;font-family:'Courgette',cursive;font-size:12.5px;color:#fff}
.newsletter .service{position:absolute;right:16px;top:109px;font-family:'Open Sans',sans-serif;font-weight:700;font-style:italic;font-size:10px;color:var(--blue-mid)}
.newsletter .headline{position:absolute;left:36px;top:131px;font-family:'Montserrat',sans-serif;font-weight:700;font-size:21px;color:var(--ink)}
.newsletter .body-col{position:absolute;left:34px;top:167px;width:123px;height:284px;overflow:hidden;font-size:6.6px;line-height:8.2px;font-weight:600;text-align:justify}
.newsletter .activities{position:absolute;left:166px;top:170px;width:91px;height:277px;background:linear-gradient(180deg,var(--blue-mid),var(--blue-bright));color:#fff;padding:6px 7px;overflow:hidden}
.newsletter .activities h3{font-size:8.5px;font-weight:700;margin-bottom:3px}
.newsletter .activities p{font-size:7px;line-height:8.7px;font-weight:600}
.newsletter .subhead{position:absolute;left:34px;top:465px;font-family:'Jost',sans-serif;font-size:17px;color:var(--blue-mid)}
.newsletter .intro{position:absolute;left:34px;top:494px;width:218px;font-size:6.8px;line-height:9.5px;font-weight:600}

/* Primary logo lockup */
.lockup{position:absolute;left:868px;top:318px;width:300px;height:260px}
.lockup .mark{left:90px;top:0;width:120px;height:120px}
.lockup .wordmark{left:0;width:300px;text-align:center}
.lockup .line1{top:176px;font-size:42px;letter-spacing:1px}
.lockup .line2{top:226px;font-size:26px;letter-spacing:5px}

/* Business card front */
.card-front{left:49px;top:790px;width:261px;height:150px;border:none;background:var(--brand-grad)}
.card-front .mark{left:111px;top:38px;width:38px;height:38px;background:#fff}
.card-front .wordmark{left:0;width:261px;text-align:center;top:88px;font-size:14px;color:#fff}
.card-front .web{left:0;width:261px;text-align:center;top:122px;color:#fff;font-size:6.5px}

/* Business card back */
.card-back{left:327px;top:790px;width:263px;height:151px}
.card-back .bar-v{left:12px;width:6px}
.card-back .bar-h{left:2px;top:27px;width:28px;height:5px}
.card-back .backdrop{position:absolute;left:196px;top:12px;width:80px;height:80px;background:var(--pale)}
.card-back .mark{left:33px;top:14px;width:22px;height:22px}
.card-back .wordmark{left:60px;top:20px;font-size:11px}
.card-back .person{position:absolute;right:18px;top:92px;text-align:right}
.card-back .name{font-family:'Jost',sans-serif;font-size:12.5px;color:var(--blue-deep);line-height:14px}
.card-back .details{font-family:'Alegreya',serif;font-size:7px;line-height:8.8px}

/* With compliments slip */
.comp-slip{left:607px;top:711px;width:491px;height:231px}
.comp-slip .bar-v{left:20px;width:6px}
.comp-slip .bar-h{left:6px;top:34px;width:35px;height:5px}
.comp-slip .mark{left:50px;top:22px;width:38px;height:38px}
.comp-slip .wordmark{left:96px;top:33px;font-size:17px}
.comp-slip .title{position:absolute;left:41px;top:164px;font-family:'Open Sans',sans-serif;font-weight:700;font-size:15px;color:var(--blue-deep)}
.comp-slip .contact{left:41px;top:187px}
.comp-slip .web{left:358px;top:206px}
</style>
</head>
<body>

<section class="sheet letterhead" aria-label="Letterhead">
  <div class="bar-v"></div>
  <div class="bar-h"></div>
  <div class="mark"></div>
  <div class="wordmark">Kereru Gospel Chapel</div>
  <p class="contact">Postal Address: PO Box 38514, Wharenui, Auckland 1893<br>Email: office@kererugospel.org.nz<br>Phone: 09 473 5619</p>
  <p class="web">www.kererugospel.org.nz</p>
</section>

<section class="sheet newsletter" aria-label="Newsletter front cover">
  <div class="header"></div>
  <div class="bar-v"></div>
  <div class="bar-h"></div>
  <p class="date">Sunday, October 4, 2014</p>
  <div class="mark"></div>
  <div class="wordmark">Kereru Gospel Chapel</div>
  <p class="tagline">“A place of Hope, Belonging and Worship”</p>
  <p class="service">Sundays @10am</p>
  <h1 class="headline">Lorem ipsum dolor</h1>
  <p class="body-col">Lorem ipsum dolor sit amet, consectetuer adipiscing elit, sed diam nonummy nibh euismod tincidunt ut laoreet dolore magna aliquam erat volutpat. Ut wisi enim ad minim veniam, quis nostrud exerci tation ullamcorper suscipit lobortis nisl ut aliquip ex ea commodo consequat. Duis autem vel eum iriure dolor in hendrerit in vulputate velit esse molestie consequat, vel illum dolore eu feugiat nulla facilisis at vero eros et accumsan et iusto odio dignissim qui blandit praesent luptatum zzril delenit augue duis dolore te feugait nulla facilisi. Nam liber tempor cum soluta nobis eleifend option congue nihil imperdiet doming id quod mazim placerat facer possim assum. Typi non habent claritatem insitam; est usus legentis in iis qui facit eorum claritatem. Investigationes demonstraverunt lectores legere me lius quod ii legunt saepius. Claritas est etiam processus dynamicus, qui sequitur mutationem consuetudium lectorum. Mirum est notare quam littera gothica, quam nunc putamus parum claram, anteposuerit litterarum formas humanitatis per seacula quarta decima et quinta decima. Eodem</p>
  <aside class="activities">
    <h3>Church Avtivities</h3>
    <p>Typi non habent claritatem insitam; est usus legentis in iis qui facit eorum claritatem. Investigationes demonstraverunt lectores legere me lius quod ii legunt saepius. Claritas est etiam processus dynamicus, qui sequitur mutationem consuetudium lectorum. Mirum est notare quam littera gothica, quam nunc putamus parum claram, anteposuerit litterarum formas humanitatis per</p>
  </aside>
  <h2 class="subhead">LOREM IPSUM DOLOR</h2>
  <p class="intro">Lorem ipsum dolor sit amet, consectetuer adipiscing elit, sed diam nonummy nibh euismod tincidunt ut laoreet dolore magna aliquam erat volutpat. Ut wisi enim ad minim veniam, quis nostrud exerci tation ullamcorper suscipit lobortis nisl ut aliquip ex ea commodo consequat. Duis autem vel eum iriure</p>
</section>

<section class="lockup" aria-label="Primary name lockup">
  <div class="mark"></div>
  <div class="wordmark line1">KERERU GOSPEL</div>
  <div class="wordmark line2">Chapel</div>
</section>

<section class="sheet card-front" aria-label="Business card front">
  <div class="mark"></div>
  <div class="wordmark">Kereru Gospel Chapel</div>
  <p class="web">www.kererugospel.org.nz</p>
</section>

<section class="sheet card-back" aria-label="Business card back">
  <div class="backdrop"></div>
  <div class="bar-v"></div>
  <div class="bar-h"></div>
  <div class="mark"></div>
  <div class="wordmark">Kereru Gospel Chapel</div>
  <div class="person">
    <p class="name">LOREM IPSUM</p>
    <p class="details">title<br>09 473 5619<br>office@kererugospel.org.nz</p>
  </div>
</section>

<section class="sheet comp-slip" aria-label="With compliments slip">
  <div class="bar-v"></div>
  <div class="bar-h"></div>
  <div class="mark"></div>
  <div class="wordmark">Kereru Gospel Chapel</div>
  <p class="title">With Compliments</p>
  <p class="contact">Postal Address: PO Box 38514, Wharenui, Auckland 1893<br>Email: office@kererugospel.org.nz<br>Phone: 09 473 5619</p>
  <p class="web">www.kererugospel.org.nz</p>
</section>

</body>
</html>
```